Organic skincare label - minimalist, earthy, luxe design needed!

I need a label design for a luxury natural skin care line called "Velka Botanix". Velka means 'earth' in Swahili. I would like the design to embody an earthy feel but be minimalistic and give a luxe vibe. My first product will be a Tumeric and Neem Scrub.

The size of the jar is 8oz, label dimensions should be (1.625" Tall x 8.5" Wide)
I will be making other products too such as; oils + toners so I feel free to do labels for glass bottles and/or spray bottles as well.

Forest green, light pinks/nudes/beige, grey, white, gold, are colors that can be used (not all have to be used).

I have included pictures of some things I've worked on myself as well as my original logo design but I need to simplify the logo, no circle around it.
Feel free to get creative.

Thank you! :)
Updates

Target Market(s)

Socially Conscious, Beauty Enthusiast, Minimalist

Industry/Entity Type

Skin Care

Font styles to use
Sans Serif
Other font styles liked:
• "Wonderlove doodle" is the font used for "Velka" in the logo. Feel free to use that or change it as you see fit.

Requirements
Must have
• Simplistic design
would like to stick to a font close to the ones in the logo. Either the one used for the name "Velka" OR the one that the slogan "Rooted Rituals" uses.

I have also included some pictures to capture the aesthetic of my social media and website.

Gender neutral

```html
<!DOCTYPE html>
<html lang="en">
<head>
<meta charset="utf-8">
<title>Velka Botanix – Rose Serum Label</title>
<link rel="stylesheet" href="https://fonts.googleapis.com/css2?family=Libre+Baskerville:wght@700&family=Open+Sans:wght@300;400&display=swap">
<style>
  :root {
    --label-bg: #e2d8d3;
    --page-bg: #ffffff;
    --grid-line: #ffffff;
    --title-ink: #5e5d55;
    --body-ink: #1f1f1f;
    --muted-ink: #6b6965;
    --badge-fill: #bcb09f;
    --badge-ink: #5e5d55;
    --leaf-light: #e6e0dc;
    --leaf-tan: #b99a86;
    --foliage-green: #4e6b45;
    --foliage-skin: #d9bfa6;
  }
  html, body {
    margin: 0;
    padding: 0;
    overflow: hidden;
    background: var(--page-bg);
  }
  .label {
    position: relative;
    width: 1200px;
    height: 230px;
    background: var(--label-bg);
    overflow: hidden;
    font-family: "Open Sans", sans-serif;
  }
  .photo-leaf {
    position: absolute;
    left: 0; top: 0;
    width: 298px; height: 230px;
    background: linear-gradient(120deg, var(--leaf-light) 0%, var(--leaf-tan) 45%, var(--leaf-light) 100%);
  }
  .photo-foliage {
    position: absolute;
    left: 1016px; top: 0;
    width: 184px; height: 230px;
    background: linear-gradient(90deg, var(--foliage-green) 0%, var(--foliage-skin) 55%, var(--foliage-green) 100%);
  }
  .grid {
    position: absolute;
    inset: 0;
    pointer-events: none;
  }
  .badge {
    position: absolute;
    left: 332px; top: 52px;
    width: 134px; height: 126px;
    border-radius: 50%;
    background: var(--badge-fill);
    text-align: center;
  }
  .badge-name {
    margin-top: 74px;
    font-size: 15px;
    font-weight: 400;
    color: var(--badge-ink);
    letter-spacing: 0.5px;
    line-height: 1;
  }
  .badge-tagline {
    margin-top: 8px;
    font-size: 5px;
    font-weight: 400;
    color: var(--badge-ink);
    letter-spacing: 0.4px;
    line-height: 1;
  }
  .product {
    position: absolute;
    left: 450px; top: 50px;
    width: 330px;
    text-align: center;
  }
  .brand-title {
    margin: 0;
    font-family: "Libre Baskerville", serif;
    font-weight: 700;
    font-size: 66px;
    line-height: 1;
    color: var(--title-ink);
    letter-spacing: 1px;
  }
  .product-name {
    margin: 16px 0 0 -8px;
    font-size: 23px;
    font-weight: 300;
    line-height: 1;
    color: var(--body-ink);
  }
  .product-name .kind { color: var(--muted-ink); }
  .volume {
    margin: 4px 0 0 -8px;
    font-size: 10.5px;
    font-weight: 300;
    line-height: 1.2;
    color: var(--body-ink);
  }
  .vertical {
    position: absolute;
    writing-mode: vertical-rl;
    transform: rotate(180deg);
    color: var(--body-ink);
    white-space: nowrap;
  }
  .ingredients {
    left: 916px; top: 46px;
    height: 162px;
    font-size: 9.8px;
    font-weight: 300;
    line-height: 14px;
  }
  .origin {
    left: 991px; top: 72px;
    height: 134px;
    font-size: 11px;
    font-weight: 400;
  }
</style>
</head>
<body>
  <div class="label">
    <div class="photo-leaf" role="img" aria-label="Photo of a dried palm leaf on a pale backdrop"></div>
    <div class="photo-foliage" role="img" aria-label="Photo of arms wrapped around green tropical leaves"></div>

    <svg class="grid" width="1200" height="230" viewBox="0 0 1200 230" aria-hidden="true">
      <line x1="0" y1="116" x2="1016" y2="116" stroke="var(--grid-line)" stroke-width="1.5" opacity="0.8"/>
      <line x1="300" y1="0" x2="300" y2="230" stroke="var(--grid-line)" stroke-width="1.5"/>
      <line x1="600" y1="0" x2="600" y2="230" stroke="var(--grid-line)" stroke-width="1.5"/>
      <line x1="900" y1="0" x2="900" y2="230" stroke="var(--grid-line)" stroke-width="1.5"/>
    </svg>

    <div class="badge">
      <div class="badge-name">Velka</div>
      <div class="badge-tagline">ROOTED RITUALS</div>
    </div>

    <div class="product">
      <h1 class="brand-title">VELKA</h1>
      <p class="product-name">ROSE <span class="kind">SERUM</span></p>
      <p class="volume">1FL OZ/ 59 ML</p>
    </div>

    <div class="vertical ingredients">INGREDIENTS:<br>ORGANIC ROSEHIP, SEED<br>OIL, ORGANIC POMGRANATE OIL,<br>VITAMIN E NON-GMO</div>
    <div class="vertical origin">MADE IN MARLOW, TX</div>
  </div>
</body>
</html>
```